goal design

We are rolling out a goal for the next 3 years. the goal is as follows:
2014: $8 million gross profit, $1.25 million net income
2015: $12 million gross profit, $2.4 million net income
2016 $15 million gross profit, $4 million net income
We want a design that captures these numbers and that we can publish company wide that will quickly remind everyone of these goals. Our website is www.brookvalerecruiting.example. This will be an internal campaign. We will use the simple design to remind our people of our goals for the next 3 years. We will print it on mouse pads, shirts and things of this nature periodically to keep it front of mind for our people. So easy to remember, visually appealing and simple are good guidelines.
Updates
Target Market(s)
This is an internal campaign. it is to remind our people of our goals for the next few years so will be on little reminder items (i.e. cell phone covers, mouse pads, shirts, screen savers, etc).
Industry/Entity Type
It Company
Look and feel

```html
<!DOCTYPE html>
<html lang="en">
<head>
<meta charset="utf-8">
<title>Three-Year Goals 2014–2016</title>
<link rel="stylesheet" href="https://fonts.googleapis.com/css2?family=Bebas+Neue&display=swap">
<style>
  :root {
    --backdrop: #2a2927;
    --ink: #2a2622;
    --gold-deep: #4a2e12;
    --gold-dark: #7a5318;
    --gold-mid: #b98a2a;
    --gold-bright: #f3d35a;
    --gold-glow: #fff0a0;
    --frame-line: #2e2a25;
    --frame-light: rgba(255, 240, 180, 0.55);
  }
  * { margin: 0; padding: 0; box-sizing: border-box; }
  html, body {
    width: 1200px;
    height: 1088px;
    overflow: hidden;
    background: var(--backdrop);
  }
  .goal-board {
    position: relative;
    width: 1200px;
    height: 1088px;
    font-family: "Bebas Neue", "Arial Narrow", sans-serif;
    color: var(--ink);
  }
  .goal-bar {
    position: absolute;
    top: 141px;
    width: 304px;
    height: 822px;
    background:
      linear-gradient(180deg, rgba(255,255,255,0.08) 0%, rgba(0,0,0,0) 30%, rgba(0,0,0,0) 70%, rgba(0,0,0,0.12) 100%),
      linear-gradient(90deg,
        var(--gold-deep) 0%,
        var(--gold-dark) 7%,
        var(--gold-mid) 20%,
        var(--gold-bright) 38%,
        var(--gold-glow) 50%,
        var(--gold-bright) 62%,
        var(--gold-mid) 80%,
        var(--gold-dark) 93%,
        var(--gold-deep) 100%);
  }
  .goal-bar--2014 { left: 131px; }
  .goal-bar--2015 { left: 469px; }
  .goal-bar--2016 { left: 805px; }

  .goal-bar__frame {
    position: absolute;
    left: 26px; right: 26px;
    top: 29px; bottom: 29px;
    border: 3px solid var(--frame-line);
    box-shadow: inset 0 0 0 3px var(--frame-light);
  }
  .goal-bar__rule {
    position: absolute;
    left: 53px; right: 53px;
    top: 196px;
    height: 3px;
    background: var(--frame-line);
    box-shadow: 0 2px 0 var(--frame-light);
  }
  .goal-line {
    position: absolute;
    left: 0; right: 0;
    text-align: center;
    line-height: 1;
    white-space: nowrap;
    text-shadow: 0 2px 0 rgba(255, 240, 170, 0.45);
  }
  .goal-year        { top: 69px;  font-size: 137px; }
  .goal-gross       { top: 204px; font-size: 199px; }
  .goal-gross-unit  { top: 384px; font-size: 78px; }
  .goal-gross-label { top: 452px; font-size: 43px; }
  .goal-net         { top: 518px; font-size: 126px; }
  .goal-net-unit    { top: 650px; font-size: 86px; }
  .goal-net-label   { top: 717px; font-size: 58px; }
</style>
</head>
<body>
<main class="goal-board">
  <section class="goal-bar goal-bar--2014">
    <div class="goal-bar__frame"></div>
    <div class="goal-bar__rule"></div>
    <h2 class="goal-line goal-year">2014</h2>
    <p class="goal-line goal-gross">$8</p>
    <p class="goal-line goal-gross-unit">Million</p>
    <p class="goal-line goal-gross-label">Gross Profit</p>
    <p class="goal-line goal-net">$1.25</p>
    <p class="goal-line goal-net-unit">Million</p>
    <p class="goal-line goal-net-label">Net Income</p>
  </section>
  <section class="goal-bar goal-bar--2015">
    <div class="goal-bar__frame"></div>
    <div class="goal-bar__rule"></div>
    <h2 class="goal-line goal-year">2015</h2>
    <p class="goal-line goal-gross">$12</p>
    <p class="goal-line goal-gross-unit">Million</p>
    <p class="goal-line goal-gross-label">Gross Profit</p>
    <p class="goal-line goal-net">$2.4</p>
    <p class="goal-line goal-net-unit">Million</p>
    <p class="goal-line goal-net-label">Net Income</p>
  </section>
  <section class="goal-bar goal-bar--2016">
    <div class="goal-bar__frame"></div>
    <div class="goal-bar__rule"></div>
    <h2 class="goal-line goal-year">2016</h2>
    <p class="goal-line goal-gross">$15</p>
    <p class="goal-line goal-gross-unit">Million</p>
    <p class="goal-line goal-gross-label">Gross Profit</p>
    <p class="goal-line goal-net">$4</p>
    <p class="goal-line goal-net-unit">Million</p>
    <p class="goal-line goal-net-label">Net Income</p>
  </section>
</main>
</body>
</html>
```